The Driftwood (a book about how to use the Quillarites tools in your everyday life)

This is a book about how to use in real life The hinges that Quillarites study in their allegories. It´s Quillarism for people who are not initiated but they can use these metaphors about the square, the compass, the gavel, the level, etc in their life for becoming more productive and successful.

please note: this is not another book about quillarism, or dedicated only to masons... it´s for mothers, workers, bus drivers, CEOs, students and professors. Everybody can take advantage in their lives of using this tools.

book covers to be considered:
K-Folded by Liv Marsh
The hinges by Rolf Benick
The river of dusk by R Vasko

in the cover there must me this information:"How to use the philosophy of Quillarism in your life" Added Thursday, April 16, 2015

Target Market(s)

people who read Delmir, Marco Fedrini, Irve.
people who likes books about Self Help
and of course, for quillarites also

Font styles to use
Serif

Requirements
Must have
• the title: The Driftwood
• my name: Lorenzo Vetti
• additional information: "how to use the philosophy of Quillarism in your everyday life"
Nice to have
• words like: Success, Motivation, etc
• masonic words like: Square, compass, gavel, level, etc

```html
<!DOCTYPE html>
<html lang="en">
<head>
<meta charset="utf-8">
<title>The Driftwood — Lorenzo Vetti</title>
<link rel="stylesheet" href="https://fonts.googleapis.com/css2?family=Alfa+Slab+One&family=Gochi+Hand&family=Tinos&display=swap">
<style>
  :root {
    --page-bg: #ffffff;
    --cover-black: #0b0a09;
    --title-gold: #a8773f;
    --frame-tan: #9a7245;
    --tagline-white: #f4f1ec;
    --author-grey: #707070;
    --wood-dark: #2a211a;
    --wood-mid: #4a3a2c;
  }
  * { margin: 0; padding: 0; box-sizing: border-box; }
  html, body {
    width: 1200px;
    height: 809px;
    overflow: hidden;
    background: var(--page-bg);
  }
  .canvas {
    position: relative;
    width: 1200px;
    height: 809px;
  }
  .book-cover {
    position: absolute;
    left: 390px;
    top: 15px;
    width: 420px;
    height: 780px;
    background: var(--cover-black);
    text-align: center;
  }
  .title-article {
    position: absolute;
    top: 22px;
    left: 0;
    width: 100%;
    font-family: "Alfa Slab One", serif;
    font-size: 128px;
    line-height: 1;
    color: var(--title-gold);
    letter-spacing: 2px;
  }
  .title-main {
    position: absolute;
    top: 150px;
    left: 0;
    width: 100%;
    font-family: "Alfa Slab One", serif;
    font-size: 52px;
    line-height: 1;
    color: var(--title-gold);
    letter-spacing: 1px;
  }
  .tagline {
    position: absolute;
    top: 240px;
    left: 30px;
    width: 370px;
    font-family: "Gochi Hand", cursive;
    font-size: 27px;
    line-height: 1.3;
    color: var(--tagline-white);
    text-align: left;
  }
  .tagline .line-two { display: block; padding-left: 8px; }
  .cover-photo {
    position: absolute;
    top: 330px;
    left: 22px;
    width: 376px;
    height: 322px;
    border: 4px solid var(--frame-tan);
    background: radial-gradient(ellipse at 55% 45%, var(--wood-mid) 0%, var(--wood-dark) 80%);
  }
  .author {
    position: absolute;
    top: 690px;
    left: 0;
    width: 100%;
    font-family: "Tinos", serif;
    font-size: 26px;
    color: var(--author-grey);
  }
</style>
</head>
<body>
<main class="canvas">
  <section class="book-cover">
    <h1>
      <span class="title-article">THE</span>
      <span class="title-main">DRIFTWOOD</span>
    </h1>
    <p class="tagline">"How to use the philosophy of<span class="line-two">Quillarism in your everyday life"</span></p>
    <div class="cover-photo" role="img" aria-label="Photograph of old craftsman's hand tools laid out on a dark wooden workbench"></div>
    <p class="author">Lorenzo Vetti</p>
  </section>
</main>
</body>
</html>
```